Business Card, Stationary with Shark Logo for Personal Injury Lawyer

I need business cards and stationery with a shark logo for my Personal Injury Law Practice. Has to have this written on it:
Martin K. Hollis
Injury Lawyer
The Corvell Building
718 Tandy Street
Providence, Rhode Island 02908
401-627-4193
Martinhollis.com

Contact Information for Business Card

Martin K. Hollis, Injury Lawyer, address, 401-627-4193, martinhollis.com

```html
<!DOCTYPE html>
<html lang="en">
<head>
<meta charset="utf-8">
<title>Martin K. Hollis – Business Card</title>
<link rel="stylesheet" href="https://fonts.googleapis.com/css2?family=Roboto:wght@400;500;700&display=swap">
<style>
  :root {
    --backdrop: #939598;
    --navy: #2a2461;
    --card-light: #f1f4f7;
    --ink-muted: #5b5b60;
    --white: #ffffff;
  }
  * { margin: 0; padding: 0; box-sizing: border-box; }
  html, body {
    width: 1200px; height: 900px; overflow: hidden;
    background: var(--backdrop);
    font-family: "Roboto", Arial, sans-serif;
  }
  .canvas { position: relative; width: 1200px; height: 900px; }
  .card { position: absolute; left: 363px; width: 475px; height: 271px; }
  .card--front { top: 145px; background: var(--navy); }
  .card--back { top: 484px; background: var(--card-light); }

  .wordmark {
    position: absolute; left: 0; right: 0;
    display: flex; align-items: center; justify-content: center; gap: 10px;
    font-weight: 700; text-transform: uppercase; letter-spacing: 0.5px;
  }
  .wordmark__square { width: 14px; height: 14px; }
  .card--front .wordmark { top: 118px; font-size: 30px; color: var(--white); }
  .card--front .wordmark__square { background: var(--white); }
  .card--back .wordmark { top: 52px; font-size: 24px; color: var(--navy); }
  .card--back .wordmark__square { background: var(--navy); width: 12px; height: 12px; }

  .identity {
    position: absolute; right: 250px; top: 180px; text-align: right;
  }
  .identity__name { font-size: 16px; font-weight: 700; color: var(--navy); line-height: 20px; }
  .identity__title { font-size: 11px; color: var(--ink-muted); line-height: 15px; }

  .divider {
    position: absolute; left: 237px; top: 157px; width: 1px; height: 81px;
    background: var(--navy);
  }
  .contact {
    position: absolute; left: 250px; top: 153px;
    font-size: 11px; color: var(--ink-muted); line-height: 15.5px;
  }
  .contact__address { margin-bottom: 11px; }
  .contact__row { display: flex; align-items: center; gap: 6px; }
  .contact__icon { width: 10px; height: 10px; flex: none; }
</style>
</head>
<body>
<main class="canvas">
  <section class="card card--front">
    <div class="wordmark"><span class="wordmark__square"></span>Martin K. Hollis</div>
  </section>

  <section class="card card--back">
    <div class="wordmark"><span class="wordmark__square"></span>Martin K. Hollis</div>

    <div class="identity">
      <p class="identity__name">MARTIN K. HOLLIS</p>
      <p class="identity__title">Injury Lawyer</p>
    </div>

    <div class="divider"></div>

    <div class="contact">
      <p class="contact__address">The Corvell Building<br>718 Tandy Street<br>Providence, Rhode Island 02908</p>
      <p class="contact__row">
        <svg class="contact__icon" viewBox="0 0 24 24" aria-hidden="true"><path fill="#2a2461" d="M6.6 10.8a15.1 15.1 0 0 0 6.6 6.6l2.2-2.2a1 1 0 0 1 1-.25 11.4 11.4 0 0 0 3.6.57 1 1 0 0 1 1 1V20a1 1 0 0 1-1 1A17 17 0 0 1 3 4a1 1 0 0 1 1-1h3.5a1 1 0 0 1 1 1c0 1.25.2 2.45.57 3.57a1 1 0 0 1-.25 1z"/></svg>
        401-627-4193
      </p>
      <p class="contact__row">
        <svg class="contact__icon" viewBox="0 0 24 24" aria-hidden="true"><g fill="none" stroke="#2a2461" stroke-width="2.4"><circle cx="12" cy="12" r="9.5"/><ellipse cx="12" cy="12" rx="4.2" ry="9.5"/><path d="M2.5 12h19M4 7h16M4 17h16"/></g></svg>
        Martinhollis.com
      </p>
    </div>
  </section>
</main>
</body>
</html>
```